Business card and stationary for a consultant firm
Sharp Compass
Professional
Renske Hoorneman
Zwaluwlaan 38
Curaçao
Renskehoorneman@postvlek.com
Zwaluwlaan38

```html
<!DOCTYPE html>
<html lang="en">
<head>
<meta charset="utf-8">
<title>Sharp Compass – Business Card Set</title>
<link href="https://fonts.googleapis.com/css2?family=Open+Sans:wght@400;600&display=swap" rel="stylesheet">
<style>
  :root {
    --frame-black: #0d0d0d;
    --board-light: #d9d9d9;
    --board-dark: #5a5a5a;
    --card-edge: #6b6b6b;
    --green: #8cc63f;
    --green-light: #b8dc78;
    --green-dark: #6fae22;
    --orange: #e0782a;
    --orange-light: #f09a52;
    --olive: #a59c1c;
    --olive-light: #c9bf52;
    --ink: #333333;
    --white: #ffffff;
  }
  * { box-sizing: border-box; margin: 0; padding: 0; }
  html, body {
    width: 1200px; height: 956px; overflow: hidden;
    background: var(--frame-black);
    font-family: "Open Sans", Arial, sans-serif;
  }
  .board {
    position: absolute; left: 73px; top: 57px; width: 1059px; height: 842px;
    background: radial-gradient(ellipse 60% 58% at 50% 48%, #f4f4f4 0%, var(--board-light) 45%, #9a9a9a 78%, var(--board-dark) 100%);
  }
  .card {
    position: absolute; border-radius: 22px; overflow: hidden;
    border: 2px solid var(--card-edge);
    box-shadow: 0 4px 10px rgba(0,0,0,.25);
  }
  /* front card */
  .card-front { left: 297px; top: 21px; width: 446px; height: 254px; background: var(--white); }
  .card-front .swoosh { position: absolute; left: 0; top: 0; width: 100%; height: 100%; }
  .brand {
    position: absolute; left: 22px; top: 20px; display: flex; align-items: center; gap: 10px;
  }
  .brand-dot { width: 42px; height: 42px; border-radius: 50%; background: var(--green); }
  .brand-name {
    font-size: 27px; font-weight: 400; color: var(--ink);
    border-left: 2px solid var(--ink); padding-left: 8px; line-height: 32px;
  }
  .holder-name {
    position: absolute; left: 0; width: 100%; top: 112px; text-align: center;
    font-size: 19px; color: var(--green-dark);
  }
  .contact {
    position: absolute; left: 20px; top: 174px; color: var(--white);
    font-size: 11px; line-height: 15px;
  }
  /* back cards */
  .card-back { width: 443px; height: 248px; display: flex; align-items: center; justify-content: center; }
  .card-back.white { left: 69px; top: 298px; background: var(--white); }
  .card-back.green { left: 528px; top: 298px; background: radial-gradient(ellipse at 40% 20%, var(--green-light), var(--green) 60%, var(--green-dark)); }
  .card-back.orange { left: 69px; top: 565px; background: radial-gradient(ellipse at 40% 20%, var(--orange-light), var(--orange) 60%); }
  .card-back.olive { left: 528px; top: 565px; background: radial-gradient(ellipse at 40% 20%, var(--olive-light), var(--olive) 65%); }
  .mark { display: flex; flex-direction: column; align-items: center; gap: 8px; }
  .mark-dot { width: 64px; height: 64px; border-radius: 50%; background: var(--orange); }
  .card-back.orange .mark-dot { background: var(--green); }
  .mark-name { font-size: 18px; font-weight: 400; color: var(--ink); }
</style>
</head>
<body>
  <main class="board">
    <section class="card card-front">
      <svg class="swoosh" viewBox="0 0 446 254" preserveAspectRatio="none" aria-hidden="true">
        <defs>
          <linearGradient id="greenBand" x1="0" y1="0" x2="0" y2="1">
            <stop offset="0" stop-color="#a9d45c"/>
            <stop offset="1" stop-color="#7dbb2c"/>
          </linearGradient>
        </defs>
        <path d="M0 190 Q200 140 446 152 L446 254 L0 254 Z" fill="url(#greenBand)"/>
        <path d="M0 186 Q200 132 446 146" fill="none" stroke="#e0782a" stroke-width="5"/>
      </svg>
      <div class="brand">
        <span class="brand-dot"></span>
        <span class="brand-name">Sharpcompass</span>
      </div>
      <p class="holder-name">Renske Hoorneman</p>
      <address class="contact">
        Zwaluwlaan 38 Curaçao<br>
        Cell: (599) 9 523 4471<br>
        Email: Renskehoorneman@postvlek.com<br>
        www.Zwaluwlaan38.com
      </address>
    </section>

    <section class="card card-back white"><div class="mark"><span class="mark-dot"></span><span class="mark-name">Sharpcompass</span></div></section>
    <section class="card card-back green"><div class="mark"><span class="mark-dot"></span><span class="mark-name">Sharpcompass</span></div></section>
    <section class="card card-back orange"><div class="mark"><span class="mark-dot"></span><span class="mark-name">Sharpcompass</span></div></section>
    <section class="card card-back olive"><div class="mark"><span class="mark-dot"></span><span class="mark-name">Sharpcompass</span></div></section>
  </main>
</body>
</html>
```